PLOV Crossway Summit Poster

We are a cellular therapy (bone marrow transplants, etc) accreditation foundation who needs a poster design for a small workshop that we are going to host within a large workshop. The workshop will 1) Educate doctors who inspect program trying to get accredited. 2) Educate programs on how to become accredited.

It will be printed and mounted on foam board for display at the PLOV booth in exhibition halls. Dimensions should be 11 x 17 inches.

Our website is www.plovsite-example.org. The design does not have to have the same theme/colors as our website.

The poster should have written:

Cellular Therapy Inspection and Accreditation Workshop
February 10th, 2015
Orvell Crossway Summit
San Diego, CA

The statement below should be in small, subtle text to allow room for the other information. All returns, italics, and trademark symbols must be used exactly as included below:

The Halvering Institute of Health Sciences, Office for Ongoing Learning is accredited by the Certification Board for Ongoing Clinical Training to provide continuing medical education for physicians.

The Halvering Institute of Health Sciences, Office for Ongoing Learning designates this live activity for a maximum of 7.5 QLB VRX Tier 1 Unit(s)™. Physicians should claim only credit commensurate with the extent of their participation in the activity.

It should also have our logo on it (I have attached 2, use the one that has the best resolution)

Let me know if there are any questions!

```html
<!DOCTYPE html>
<html lang="en">
<head>
<meta charset="utf-8">
<title>PLOV Cellular Therapy Workshop Poster</title>
<link rel="stylesheet" href="https://fonts.googleapis.com/css2?family=Montserrat:wght@600;700&family=Arimo:ital,wght@0,400;0,700;1,400&display=swap">
<style>
  :root {
    --red: #e3101d;
    --teal: #2b6b70;
    --teal-band: #3a9697;
    --strip-light: #6fe8dc;
    --strip-mid: #3e9a9c;
    --strip-dark: #2e6c70;
    --ink: #3a3a3a;
    --rule: #8a8a8a;
    --navy: #0f3559;
    --navy-deep: #0a2745;
    --white: #ffffff;
  }
  * { margin: 0; padding: 0; box-sizing: border-box; }
  html, body { width: 1000px; height: 1200px; overflow: hidden; background: var(--white); }
  .poster {
    position: absolute; left: 112px; top: 0; width: 776px; height: 1200px;
    font-family: "Arimo", Arial, sans-serif; overflow: hidden;
  }
  .top-strip { position: absolute; left: 0; top: 0; width: 100%; height: 22px; display: flex; }
  .top-strip span:nth-child(1) { width: 86px; background: var(--strip-light); }
  .top-strip span:nth-child(2) { width: 108px; background: var(--strip-mid); }
  .top-strip span:nth-child(3) { flex: 1; background: var(--strip-dark); }
  .hero {
    position: absolute; left: 0; top: 22px; width: 100%; height: 783px;
    background:
      radial-gradient(ellipse 60% 50% at 25% 28%, #ffffff 0%, rgba(255,255,255,0.92) 45%, rgba(255,255,255,0) 80%),
      linear-gradient(100deg, rgba(255,255,255,0) 55%, rgba(190,225,140,0.55) 80%, rgba(150,220,210,0.5) 100%),
      linear-gradient(180deg, #f6fbf3 0%, #eff7df 35%, #dcefc4 55%, #ade3d6 78%, #80cde0 100%);
  }
  .brand {
    position: absolute; left: 42px; top: 78px;
    font-family: "Montserrat", sans-serif; font-weight: 600;
    font-size: 78px; color: var(--red); letter-spacing: 2px; line-height: 1;
  }
  .rule { position: absolute; left: 38px; width: 530px; height: 3px; background: var(--rule); }
  .rule.upper { top: 250px; }
  .rule.lower { top: 521px; }
  .title {
    position: absolute; left: 38px; top: 280px;
    font-family: "Montserrat", sans-serif; font-weight: 700; color: var(--red);
    font-size: 47px; line-height: 1; letter-spacing: -0.8px;
  }
  .subtitle {
    position: absolute; left: 40px; top: 330px;
    font-family: "Montserrat", sans-serif; font-weight: 700; color: var(--teal);
    font-size: 19.8px; letter-spacing: -0.3px;
  }
  .event { position: absolute; left: 38px; top: 378px; color: var(--ink); font-weight: 700; }
  .event .big { font-size: 30px; line-height: 36px; }
  .event .small { font-size: 23px; line-height: 30px; }
  .tracks { position: absolute; left: 38px; top: 574px; width: 625px; color: var(--ink); }
  .tracks h2 { font-size: 26px; color: var(--red); font-weight: 700; margin-bottom: 12px; }
  .tracks ul { list-style: none; }
  .tracks li { font-size: 17px; line-height: 24px; padding-left: 17px; text-indent: -13px; margin-bottom: 12px; }
  .tracks li::before { content: "\2022"; margin-right: 5px; }
  .tracks strong { color: var(--teal); font-size: 18px; }
  .credits-panel {
    position: absolute; left: 0; top: 805px; width: 100%; height: 331px;
    background: radial-gradient(ellipse 60% 80% at 30% 40%, #164773 0%, var(--navy) 55%, var(--navy-deep) 100%);
    box-shadow: inset 0 6px 8px rgba(0,0,0,0.25);
  }
  .credits-text { position: absolute; left: 38px; top: 44px; width: 420px; color: var(--white); font-size: 14.3px; line-height: 25.5px; }
  .credits-text p + p { margin-top: 24px; }
  .photo-frame {
    position: absolute; left: 470px; top: 41px; width: 266px; height: 252px;
    background: var(--white); padding: 6px; border-radius: 4px; box-shadow: 0 3px 10px rgba(0,0,0,0.5);
  }
  .photo-fill { width: 100%; height: 100%; background: linear-gradient(180deg, #cfe0f2 0%, #e8eef4 35%, #9fa9b0 58%, #3e6f9e 68%, #2a5f93 100%); }
  .register {
    position: absolute; left: 0; top: 1136px; width: 100%; height: 64px;
    background: var(--teal-band); color: var(--white); text-align: center;
    font-size: 25px; font-weight: 700; line-height: 64px; text-shadow: 0 1px 2px rgba(0,0,0,0.35);
  }
</style>
</head>
<body>
<main class="poster">
  <div class="top-strip"><span></span><span></span><span></span></div>
  <section class="hero">
    <div class="brand">PLOV</div>
    <div class="rule upper"></div>
    <h1 class="title">CELLULAR THERAPY</h1>
    <div class="subtitle">INSPECTION AND ACCREDITATION WORKSHOP</div>
    <div class="event">
      <div class="big">Orvell Crossway Summit</div>
      <div class="big">February 10, 2015</div>
      <div class="small">Harborline Grand Hotel</div>
      <div class="small">San Diego, CA</div>
    </div>
    <div class="rule lower"></div>
    <div class="tracks">
      <h2>Educational Tracks</h2>
      <ul>
        <li>The <strong>Inspector Track</strong> will provide PLOV Inspectors guidance on how to thoroughly, efficiently, and professionally assess compliance with the Standards.</li>
        <li>The <strong>Applicant Track</strong> will give programs and facilities insight into how to maintain and demonstrate compliance with PLOV Standards.</li>
      </ul>
    </div>
  </section>
  <section class="credits-panel">
    <div class="credits-text">
      <p>The Halvering Institute of Health Sciences, Office for Ongoing Learning is accredited by the Certification Board for Ongoing Clinical Training to provide continuing medical education for physicians.</p>
      <p>The Halvering Institute of Health Sciences, Office for Ongoing Learning designates this live activity for a maximum of <em>7.5 QLB VRX Tier 1 Unit(s)™</em>. Physicians should claim only credit commensurate with the extent of their participation in the activity.</p>
    </div>
    <div class="photo-frame">
      <div class="photo-fill" role="img" aria-label="Photo of the San Diego waterfront skyline with hotel towers across the bay"></div>
    </div>
  </section>
  <footer class="register">Register at www.plovsite-example.org</footer>
</main>
</body>
</html>
```